Tequila Bottle Labels

We are a construction company that bottled our own tequila and would like a unique label for it! We already have our own company logo (linked below) and we want that logo somewhere on the bottle as well- it can be big or small. It was brewed & bottled in Southern California. Ideally it would have the year "2020," "Single Estate," & "100% Agave Azul" somewhere on the label.

Tequila / RMT / 2020

```html
<!DOCTYPE html>
<html lang="en">
<head>
<meta charset="utf-8">
<title>Tequila 2020 – RMT Label</title>
<link rel="stylesheet" href="https://fonts.googleapis.com/css2?family=Almendra:wght@700&family=Cormorant+Garamond:wght@600;700&display=swap">
<style>
  :root {
    --backdrop: #e9e9e7;
    --label-paper: #fbfbf9;
    --agave-blue: #1d3f7c;
    --frame-blue: #2a4c86;
    --leaf-green: #7cbf2a;
    --sketch-tone: #d3dbe5;
    --white: #ffffff;
  }
  * { box-sizing: border-box; margin: 0; padding: 0; }
  html, body {
    width: 802px;
    height: 1200px;
    overflow: hidden;
    background: var(--backdrop);
  }
  .label {
    position: absolute;
    left: 41px;
    top: 155px;
    width: 720px;
    height: 890px;
    background: var(--label-paper);
    border-radius: 40px;
    box-shadow: 0 2px 10px rgba(0,0,0,0.08);
  }
  .label-frame {
    position: absolute;
    inset: 14px;
    border: 3px solid var(--frame-blue);
    border-radius: 30px;
  }
  .agave-sketch {
    position: absolute;
    left: 30px;
    top: 30px;
    width: 260px;
    height: 230px;
    border-radius: 20px 20px 120px 20px;
    background: radial-gradient(ellipse at 40% 45%, var(--sketch-tone) 0%, rgba(211,219,229,0.3) 55%, rgba(251,251,249,0) 80%);
  }
  .wordmark {
    position: absolute;
    left: 0;
    right: 0;
    top: 230px;
    text-align: center;
    font-family: "Almendra", serif;
    font-weight: 700;
    font-size: 124px;
    line-height: 1;
    color: var(--agave-blue);
    letter-spacing: 1px;
  }
  .vintage {
    position: absolute;
    right: 150px;
    top: 370px;
    font-family: "Cormorant Garamond", serif;
    font-weight: 700;
    font-size: 46px;
    line-height: 1;
    color: var(--leaf-green);
    letter-spacing: 2px;
  }
  .harvest-illustration {
    position: absolute;
    left: 250px;
    top: 470px;
    width: 230px;
    height: 170px;
    border-radius: 80px 80px 20px 20px;
    background: linear-gradient(180deg, rgba(211,219,229,0.15) 0%, var(--sketch-tone) 100%);
  }
  .agave-band {
    position: absolute;
    left: 17px;
    right: 17px;
    top: 672px;
    height: 64px;
    background: var(--agave-blue);
    display: flex;
    align-items: center;
    justify-content: center;
    gap: 22px;
  }
  .agave-band-text {
    font-family: "Cormorant Garamond", serif;
    font-weight: 700;
    font-size: 40px;
    line-height: 1;
    color: var(--white);
    letter-spacing: 2px;
  }
  .band-rule {
    width: 80px;
    height: 2px;
    background: var(--white);
  }
  .maker {
    position: absolute;
    left: 0;
    right: 0;
    top: 752px;
    text-align: center;
  }
  .maker-name {
    font-family: "Cormorant Garamond", serif;
    font-weight: 700;
    font-size: 66px;
    line-height: 1;
    color: var(--agave-blue);
    letter-spacing: 3px;
  }
  .maker-tagline {
    margin-top: 4px;
    font-family: "Cormorant Garamond", serif;
    font-weight: 700;
    font-size: 18px;
    line-height: 1;
    color: var(--leaf-green);
    letter-spacing: 1px;
  }
</style>
</head>
<body>
  <main class="label">
    <div class="label-frame"></div>
    <div class="agave-sketch" role="img" aria-label="Faint line sketch of blue agave leaves"></div>
    <h1 class="wordmark">Tequila</h1>
    <div class="vintage">2020</div>
    <div class="harvest-illustration" role="img" aria-label="Line drawing of a hand holding agave hearts"></div>
    <div class="agave-band">
      <span class="band-rule"></span>
      <span class="agave-band-text">100% AGAVE AZUL</span>
      <span class="band-rule"></span>
    </div>
    <div class="maker">
      <div class="maker-name">RMT</div>
      <div class="maker-tagline">Single Estate</div>
    </div>
  </main>
</body>
</html>
```